Varenholt Windows & Doors

We are an aluminum windows & doors manufacturer. Need a professional & vision appealing web design. It should reflects our professional business character, but with very user-friendly interface( catch eyes, use simple icon or symbol to make it easy to read...) Don't copy : ) but can use some competitor's web (https://www.polkrenwindows.example) (www.brivatglazing.example.au) to have a glance on our target and web content as reference

Target Market(s)

Homeowner and Professional (Builder / Developer/ Architect & window installer)

Industry/Entity Type

Manufacturer

Font styles to use
Serif
Sans Serif

Requirements
Must have
• Have 3 serials products. Residential (value for money) Commercial (Professional and quality) Architectural (Bold & funky)
• Color match or harmony with the selected logo design
Nice to have
• Project gallery display, have online free quote to upload files, can insert video or cartoon
Should not have
• no limitation on your imagination ; )

```html
<!DOCTYPE html>
<html lang="en">
<head>
<meta charset="utf-8">
<title>Varenholt Windows &amp; Doors</title>
<link rel="stylesheet" href="https://fonts.googleapis.com/css2?family=Open+Sans:wght@400;600&family=Roboto+Condensed:wght@400&display=swap">
<style>
:root{
  --green:#8cc63f;
  --green-dark:#6fa52a;
  --ink:#222;
  --text:#555;
  --grey-band:#eceeef;
  --white:#fff;
  --footer:#1e1f1f;
  --footer-text:#c9c9c9;
}
*{box-sizing:border-box;margin:0;padding:0}
html,body{width:1200px;height:3041px;overflow:hidden}
body{position:relative;background:var(--white);font-family:"Open Sans",Arial,sans-serif;color:var(--ink)}
.abs{position:absolute}

/* Top bar */
.topbar{left:416px;top:0;width:784px;height:40px;background:var(--green);clip-path:polygon(20px 0,100% 0,100% 100%,0 100%);color:#fff;font-size:15px}
.topbar .info{position:absolute;top:10px;display:flex;align-items:center;gap:8px}
.topbar .phone{left:64px}
.topbar .mail{left:234px}
.topbar .social{position:absolute;right:94px;top:12px;display:flex;gap:8px}
.topbar .social span{width:15px;height:15px;background:#fff;border-radius:3px;opacity:.95}

/* Header */
.logo{left:120px;top:76px;display:flex;align-items:center;gap:12px}
.logo .mark{width:34px;height:34px;background:var(--green)}
.logo .name{font-size:26px;font-weight:600;color:var(--green);letter-spacing:1px}
.nav{left:432px;top:85px;display:flex;gap:31px;font-size:16px;color:#222}
.nav .active{color:var(--green)}
.nav .search{width:18px;height:18px;margin-top:2px}

/* Hero */
.hero{left:0;top:146px;width:1200px;height:502px;background:linear-gradient(180deg,#4a4d50 0%,#6d7174 45%,#3a3c3e 100%)}
.hero-window{left:805px;top:220px;width:262px;height:343px;background:linear-gradient(135deg,#f4f5f6,#cfd3d6)}
.hero-title{left:182px;top:330px;font-size:74px;font-weight:600;letter-spacing:9px;color:#fff}
.hero-sub{left:180px;top:420px;font-family:"Roboto Condensed",Arial,sans-serif;font-size:23px;color:#fff}
.hero-arrows{left:182px;top:476px;display:flex;gap:8px}
.hero-arrows span{width:22px;height:22px;border-radius:50%;background:#fff;display:flex;align-items:center;justify-content:center}

/* Products */
.products-band{left:0;top:648px;width:1200px;height:280px;background:var(--grey-band)}
.section-title{width:1200px;left:0;text-align:center;font-size:32px;font-weight:400;color:#111;letter-spacing:.5px}
.diamond{width:206px;height:206px;border-radius:24px;transform:rotate(45deg);background:#fff;box-shadow:6px 8px 0 var(--green),0 10px 30px rgba(0,0,0,.12)}
.diamond.is-active{background:var(--green);box-shadow:6px 8px 0 #1b1b1b,0 10px 30px rgba(0,0,0,.15)}
.diamond-label{width:260px;text-align:center;font-size:20px;color:#222}
.diamond-label.is-active{color:#fff}
.diamond-icon{width:60px;height:60px}

/* Welcome */
.welcome{left:111px;top:1196px;width:978px;height:334px;background:#fff;box-shadow:0 6px 40px rgba(0,0,0,.14)}
.welcome-media{left:523px;top:0;width:455px;height:334px;background:linear-gradient(160deg,#e9eef2 0%,#c9b79a 50%,#eef0f1 100%)}
.welcome h2{position:absolute;left:60px;top:72px;font-size:28px;font-weight:400;color:#111}
.welcome p{position:absolute;left:60px;top:118px;width:410px;font-size:13.5px;line-height:22.5px;color:var(--text);text-align:justify}
.btn-more{position:absolute;left:61px;top:251px;width:110px;height:36px;border-radius:18px;background:var(--green);color:#fff;font-size:11px;display:flex;align-items:center;justify-content:center;letter-spacing:.5px}
.play{left:194px;top:134px;width:66px;height:66px;border-radius:50%;background:rgba(40,40,40,.7);display:flex;align-items:center;justify-content:center}

/* Gallery */
.gallery-band{left:0;top:1658px;width:1200px;height:130px;background:#efefef}
.gallery{left:0;top:1788px;width:1200px;display:grid;grid-template-columns:repeat(4,300px);grid-auto-rows:235px}
.gallery div{border:1px solid rgba(255,255,255,.4)}
.g1{background:linear-gradient(160deg,#8fb3d3,#4d5f70)}
.g2{background:linear-gradient(160deg,#e9e7e0,#b9b3a4)}
.g3{background:linear-gradient(180deg,#f4f4f4,#b6bcc0)}
.g4{background:linear-gradient(160deg,#6b4a33,#b49775)}
.g5{background:linear-gradient(160deg,#2f3d4b,#7d8a96)}
.g6{background:linear-gradient(150deg,#cfe0ea,#5d7a90)}
.g7{background:linear-gradient(180deg,#9fbcd2,#e8e6e2)}
.g8{background:linear-gradient(160deg,#8a7c6c,#3b3430)}

/* Contact */
.contact{left:0;top:2258px;width:1200px;height:474px;background:linear-gradient(180deg,#84c23a,#95cc4c)}
.contact .section-title{top:96px;color:#fff}
.field{background:#fff;height:57px;font-size:14px;color:#333;padding:16px 18px;box-shadow:0 2px 4px rgba(0,0,0,.2)}
.btn-submit{left:547px;top:349px;width:144px;height:40px;border-radius:20px;background:#111;color:#fff;font-size:16px;display:flex;align-items:center;justify-content:center}

/* Footer */
.footer{left:0;top:2732px;width:1200px;height:309px;background:var(--footer);color:var(--footer-text)}
.footer-logo{left:87px;top:92px;display:flex;align-items:center;gap:10px}
.footer-logo .mark{width:28px;height:28px;background:var(--green)}
.footer-logo .name{font-size:22px;font-weight:600;color:var(--green);letter-spacing:1px}
.fcol{top:73px}
.fcol h4{font-size:15px;font-weight:400;color:#eee;margin-bottom:12px}
.fcol li{list-style:none;font-size:11px;line-height:23.5px}
.fcol li::before{content:"»";margin-right:6px;color:#ddd}
.fcol.contact-col li::before{content:none}
.fcol.contact-col li{display:flex;align-items:center;gap:6px;font-size:12px;line-height:24px}
.footer-rule{left:87px;top:218px;width:1026px;height:1px;background:#3a3a3a}
.copy{left:87px;top:254px;font-size:11px}
.fsocial{left:910px;top:248px;display:flex;gap:10px}
.fsocial span{width:25px;height:25px;border-radius:50%;border:1.5px solid #aaa}
</style>
</head>
<body>

<!-- Top bar -->
<div class="abs topbar">
  <div class="info phone">
    <svg width="14" height="14" viewBox="0 0 24 24"><rect x="1" y="1" width="22" height="22" rx="4" fill="#fff"/><path d="M8 6l2 3-1.5 1.5a8 8 0 0 0 5 5L15 14l3 2-1 2.5c-5 0-10-5-10-10z" fill="#8cc63f"/></svg>
    <span>: (555) 014 - 2780</span>
  </div>
  <div class="info mail">
    <svg width="15" height="12" viewBox="0 0 24 18"><rect width="24" height="18" rx="2" fill="#fff"/><path d="M2 2l10 8 10-8" stroke="#8cc63f" stroke-width="2" fill="none"/></svg>
    <span>: info@varenholt.example</span>
  </div>
  <div class="social"><span></span><span></span><span></span><span></span></div>
</div>

<!-- Header -->
<div class="abs logo"><span class="mark"></span><span class="name">VARENHOLT</span></div>
<nav class="abs nav">
  <span class="active">Home</span><span>About us</span><span>Services</span><span>Products</span><span>Gallery</span><span>Blog</span><span>Contact us</span>
  <svg class="search" viewBox="0 0 24 24"><circle cx="10" cy="10" r="7" stroke="#111" stroke-width="3" fill="none"/><path d="M15 15l6 6" stroke="#111" stroke-width="3"/></svg>
</nav>

<!-- Hero -->
<div class="abs hero" role="img" aria-label="Modern interior with floor-to-ceiling aluminium windows"></div>
<div class="abs hero-window" role="img" aria-label="White double casement window product"></div>
<h1 class="abs hero-title">VARENHOLT</h1>
<p class="abs hero-sub">We are an aluminum windows &amp; doors manufacturer.</p>
<div class="abs hero-arrows">
  <span><svg width="10" height="10" viewBox="0 0 10 10"><path d="M6.5 1.5L3 5l3.5 3.5" stroke="#222" stroke-width="1.8" fill="none"/></svg></span>
  <span><svg width="10" height="10" viewBox="0 0 10 10"><path d="M3.5 1.5L7 5 3.5 8.5" stroke="#222" stroke-width="1.8" fill="none"/></svg></span>
</div>

<!-- Products -->
<div class="abs products-band"></div>
<h2 class="abs section-title" style="top:692px">OUR PRODUCTS</h2>

<div class="abs diamond is-active" style="left:167px;top:826px"></div>
<div class="abs diamond" style="left:475px;top:826px"></div>
<div class="abs diamond" style="left:789px;top:826px"></div>

<svg class="abs diamond-icon" style="left:240px;top:860px" viewBox="0 0 60 60" fill="none" stroke="#fff" stroke-width="2.2">
  <path d="M12 56V26a18 18 0 0 1 36 0v30z"/><path d="M18 50V27a12 12 0 0 1 24 0v23z"/><path d="M30 15v35M18 33h24"/><path d="M8 56h44"/>
</svg>
<svg class="abs diamond-icon" style="left:548px;top:860px" viewBox="0 0 60 60" fill="none" stroke="#222" stroke-width="2.2">
  <rect x="12" y="4" width="36" height="50"/><rect x="17" y="9" width="26" height="16"/><path d="M17 25l10-16M30 25l10-16"/><rect x="17" y="29" width="26" height="20"/><path d="M8 56h44"/>
</svg>
<svg class="abs diamond-icon" style="left:862px;top:860px" viewBox="0 0 60 60" fill="none" stroke="#222" stroke-width="2.2">
  <path d="M6 54L54 8v46z"/><path d="M22 46l24-23v23z"/><path d="M10 26l18-18 4 4-18 18z"/><path d="M40 54v-5M46 54v-5"/>
</svg>

<div class="abs diamond-label is-active" style="left:140px;top:953px">Residential</div>
<div class="abs diamond-label" style="left:448px;top:953px">Commercial</div>
<div class="abs diamond-label" style="left:762px;top:953px">Architectural</div>

<!-- Welcome -->
<section class="abs welcome">
  <h2>WELCOME TO VARENHOLT</h2>
  <p>It is a long established fact that a reader will be distracted by the readable content of a page when looking at its layout. The point of using Lorem Ipsum is that it has a more-or-less normal distribution of letters, as opposed to using 'Content here, content here', making it look like readable English.</p>
  <span class="btn-more">READ MORE</span>
  <div class="abs welcome-media" role="img" aria-label="Video still of a modern family house with large aluminium windows">
    <div class="abs play"><svg width="24" height="26" viewBox="0 0 24 26"><path d="M4 2l18 11L4 24z" fill="#fff"/></svg></div>
  </div>
</section>

<!-- Gallery -->
<div class="abs gallery-band"></div>
<h2 class="abs section-title" style="top:1703px">PROJECT GALLERY</h2>
<div class="abs gallery">
  <div class="g1" role="img" aria-label="Glass-fronted commercial building"></div>
  <div class="g2" role="img" aria-label="Close-up of a white window frame"></div>
  <div class="g3" role="img" aria-label="Sliding glass doors in an office"></div>
  <div class="g4" role="img" aria-label="Timber-look folding doors opening to a garden"></div>
  <div class="g5" role="img" aria-label="Glazed shopfront entrance"></div>
  <div class="g6" role="img" aria-label="Curtain wall facade seen from below"></div>
  <div class="g7" role="img" aria-label="Living room with panoramic windows"></div>
  <div class="g8" role="img" aria-label="Installer fitting an aluminium frame"></div>
</div>

<!-- Contact -->
<section class="abs contact">
  <h2 class="abs section-title">CONTACT US</h2>
  <div class="abs field" style="left:152px;top:187px;width:300px">Name</div>
  <div class="abs field" style="left:470px;top:187px;width:302px">Email id</div>
  <div class="abs field" style="left:789px;top:187px;width:300px">Phone</div>
  <div class="abs field" style="left:152px;top:256px;width:937px">Message</div>
  <span class="abs btn-submit">SUBMIT</span>
</section>

<!-- Footer -->
<footer class="abs footer">
  <div class="abs footer-logo"><span class="mark"></span><span class="name">VARENHOLT</span></div>
  <div class="abs fcol" style="left:379px"><h4>links</h4><ul><li>Home</li><li>Services</li><li>Recent Projects</li><li>About us</li></ul></div>
  <div class="abs fcol" style="left:533px"><h4>Information</h4><ul><li>Privacy Policy</li><li>Login</li><li>Advanced Search</li><li>Contact Us</li></ul></div>
  <div class="abs fcol" style="left:710px"><h4>Quicklink</h4><ul><li>Products</li><li>Residential</li><li>Commercial</li><li>Architectural</li></ul></div>
  <div class="abs fcol contact-col" style="left:900px"><h4>Contact</h4><ul>
    <li><svg width="10" height="13" viewBox="0 0 10 14"><path d="M5 0a5 5 0 0 1 5 5c0 4-5 9-5 9S0 9 0 5a5 5 0 0 1 5-5z" fill="#ddd"/><circle cx="5" cy="5" r="2" fill="#1e1f1f"/></svg>420 Larkspur Rd, Fairmont, IL 60000</li>
    <li><svg width="12" height="12" viewBox="0 0 24 24"><path d="M5 2l4 5-2.5 2.5a12 12 0 0 0 8 8L17 15l5 4-2 3C10 22 2 14 2 4z" fill="#ddd"/></svg>(555) 013-6619</li>
    <li><svg width="13" height="10" viewBox="0 0 24 18"><rect width="24" height="18" rx="2" fill="#ddd"/><path d="M2 2l10 8 10-8" stroke="#1e1f1f" stroke-width="2" fill="none"/></svg>info@varenholt.example</li>
  </ul></div>
  <div class="abs footer-rule"></div>
  <p class="abs copy">Copyright © 2017. All Rights Reserved</p>
  <div class="abs fsocial"><span></span><span></span><span></span><span></span><span></span><span></span></div>
</footer>

</body>
</html>
```